Re-branding for Structural Engineering firm

We need new business cards as part of our current re-branding. We have a new logo (attached), so the card design should incorporate this color scheme. We are a structural engineering firm providing structural building design and seismic consulting services. The final design should communicate professionalism and stability, with a modern look and feel.

```html
<!DOCTYPE html>
<html lang="en">
<head>
<meta charset="utf-8">
<title>Harlow Structural Engineering – Business Cards</title>
<link rel="stylesheet" href="https://fonts.googleapis.com/css2?family=Lato:wght@400;700;900&display=swap">
<style>
  :root {
    --brand-blue: #1a70b8;
    --brand-grey: #76787b;
    --arc-grey: #8c8d90;
    --card-white: #ffffff;
    --card-shade: #eceded;
    --ink-soft: #6d6f72;
    --backdrop: #e4e5e7;
  }
  * { margin: 0; padding: 0; box-sizing: border-box; }
  html, body {
    width: 1200px; height: 997px; overflow: hidden;
    background: var(--backdrop);
    font-family: "Lato", Arial, sans-serif;
  }
  .sheet {
    position: relative; width: 1200px; height: 997px;
    display: flex; flex-direction: column; align-items: center; justify-content: center; gap: 60px;
  }
  .card {
    position: relative; width: 700px; height: 400px;
    border-radius: 22px; overflow: hidden;
    background: linear-gradient(160deg, var(--card-white) 40%, var(--card-shade));
    box-shadow: 0 10px 30px rgba(0,0,0,0.18);
  }
  .card__swoosh { position: absolute; inset: 0; width: 100%; height: 100%; }
  .band { fill: var(--brand-blue); }
  .arc { fill: var(--arc-grey); }

  .wordmark { display: flex; align-items: center; gap: 14px; color: var(--brand-blue); font-weight: 900; }
  .wordmark__square { background: var(--brand-blue); flex: none; }
  .wordmark__name { text-transform: uppercase; line-height: 1.05; letter-spacing: 0.5px; }

  /* front */
  .card--front .wordmark { position: absolute; left: 190px; top: 95px; }
  .card--front .wordmark__square { width: 58px; height: 58px; }
  .card--front .wordmark__name { font-size: 30px; }
  .card--front .website {
    position: absolute; right: 40px; top: 318px;
    color: var(--card-white); font-weight: 700; font-size: 19px; letter-spacing: 1px;
    transform: rotate(-4deg);
  }

  /* back */
  .card--back .wordmark { position: absolute; right: 40px; top: 34px; }
  .card--back .wordmark__square { width: 30px; height: 30px; }
  .card--back .wordmark__name { font-size: 16px; }
  .person { position: absolute; left: 44px; top: 178px; transform: rotate(-6deg); transform-origin: left top; }
  .person__name { color: var(--brand-blue); font-size: 24px; font-weight: 400; letter-spacing: 1.5px; text-transform: uppercase; }
  .person__role { color: var(--ink-soft); font-size: 14px; margin-top: 2px; }
  .contacts { position: absolute; left: 44px; top: 285px; list-style: none; }
  .contacts__item { display: flex; align-items: center; gap: 14px; color: var(--card-white); font-size: 16px; height: 34px; }
  .contacts__icon { width: 22px; height: 22px; border-radius: 50%; background: var(--card-white); display: flex; align-items: center; justify-content: center; }
  .contacts__icon svg { width: 12px; height: 12px; fill: var(--brand-blue); }
</style>
</head>
<body>
<main class="sheet">

  <section class="card card--back" aria-label="Business card, contact side">
    <svg class="card__swoosh" viewBox="0 0 700 400" aria-hidden="true">
      <path class="arc" d="M0,248 Q370,150 700,148 L700,160 Q380,166 0,262 Z"/>
      <path class="band" d="M0,272 Q380,178 700,174 L700,400 L0,400 Z"/>
    </svg>
    <div class="wordmark">
      <span class="wordmark__square"></span>
      <span class="wordmark__name">Harlow<br>Structural Engineering</span>
    </div>
    <div class="person">
      <p class="person__name">Daniel Ashford</p>
      <p class="person__role">Managing Director</p>
    </div>
    <ul class="contacts">
      <li class="contacts__item">
        <span class="contacts__icon"><svg viewBox="0 0 12 12"><path d="M2.5 1h2l1 2.5-1.3 1a6 6 0 0 0 3.3 3.3l1-1.3L11 7.5v2A1.5 1.5 0 0 1 9.5 11 8.5 8.5 0 0 1 1 2.5 1.5 1.5 0 0 1 2.5 1z"/></svg></span>
        +1 (555) 014-2290
      </li>
      <li class="contacts__item">
        <span class="contacts__icon"><svg viewBox="0 0 12 12"><path d="M1 2.5h10v7H1z M1.5 3l4.5 3.5L10.5 3" stroke="#fff" stroke-width="0.8"/></svg></span>
        daniel@harlowstructural.com
      </li>
      <li class="contacts__item">
        <span class="contacts__icon"><svg viewBox="0 0 12 12"><circle cx="6" cy="6" r="5"/><path d="M1 6h10M6 1c-2 2.5-2 7.5 0 10M6 1c2 2.5 2 7.5 0 10" stroke="#fff" stroke-width="0.7" fill="none"/></svg></span>
        harlowstructural.com
      </li>
    </ul>
  </section>

  <section class="card card--front" aria-label="Business card, brand side">
    <svg class="card__swoosh" viewBox="0 0 700 400" aria-hidden="true">
      <path class="arc" d="M205,400 Q450,262 700,252 L700,264 Q460,280 232,400 Z"/>
      <path class="band" d="M245,400 Q480,292 700,282 L700,400 Z"/>
    </svg>
    <div class="wordmark">
      <span class="wordmark__square"></span>
      <span class="wordmark__name">Harlow<br>Structural Engineering</span>
    </div>
    <p class="website">www.harlowstructural.com</p>
  </section>

</main>
</body>
</html>
```